Need a powerful, eye-catching book cover design for a Public Relations book for Lawyers.

We need a beautiful, elegant, and professional cover for a public relations book. We’ll be selling this both to (1) creative, experienced legal marketers, and (2) conservative lawyers. It must grab their attention visually, and have a bold, easy to read headline. The cover image may wrap around to the back cover.SIZE: 6 x 9” 100 pagesTITLE: The Ultimate Public Relations Handbook for LawyersSUBHEAD: Make millions using media and the InternetCO-AUTHORSRoss Fishman, JDJohn HellermanInclude a CALLOUT quote: “The definitive PR book. Simple and powerful.” – Tad Lurvey, SkaddenGRAPHICS:You may use one of the attached photos, crop or flip them however you’d like, or use something else entirely. DESCRIPTION for the back cover:Why do some law firms have the best reputations or command the highest hourly rates? Why are some the go-to firms or thought leaders in particular specialties? Why are your competitors in the media more than you? Two words: Public relations. The co-authors are known worldwide as leaders in public relations, legal marketing, and branding. Neil Stamford is called, “A PR Guru.” Bar Ledger magazine wrote ““Many people consider Dale Warbeck to be the nation’s foremost expert on law firm marketing.”Tad Lurvey built Brommick into the first firm to generate $1 billion in revenue. Yvonne Pelstrup is the nation’s go-to lawyer for women’s issues. Your home town’s top PI lawyer gets the first look at the biggest cases. Why? Strategic, intentional, effective PR. Are you tired of toiling in anonymity? Want to earn the attention of reporters and editors who can build your credentials and reputation for expertise? Wouldn’t it be nice to have more clients begging you to represent them because they heard you were the best in town? That is what public relations is designed to do. Want to get more respect, earn more clients, and charge higher rates? Get known as a thought leader in a specialty practice or industry? Public relations could be your most-important marketing tool. And this book will teach you precisely how. Ready to catapult your practice to new heights? Take a deep breath and dive in….

Target Market(s)

1. Creative marketing professionals
2. Conservative 40-year-old lawyers

Industry/Entity Type

Legal

Font styles to use
Serif

Requirements
Must have
• Want a simple, bold, eye catching design conveying professionalism and quality. This is a practical, how-to book. We need a simple design and strong headline that will work well at a small thumbnail size on Zelbora.
Nice to have
• Perhaps the microphone could wrap around the cover? A tight crop of a microphone that creates an abstract could work. Let's create something memorable.

```html
<!DOCTYPE html>
<html lang="en">
<head>
<meta charset="utf-8">
<title>The Complete Press Outreach Manual for Attorneys – Cover Wrap</title>
<link rel="stylesheet" href="https://fonts.googleapis.com/css2?family=Barlow+Semi+Condensed:ital,wght@0,600;0,700;1,600&family=Catamaran:wght@400;500;600;700&display=swap">
<style>
  :root {
    --page-bg: #eeece7;
    --cover-deep: #2f78a8;
    --cover-mid: #3d86b5;
    --cover-light: #5a9cc4;
    --ink-white: #ffffff;
    --accent-yellow: #f1d54c;
    --accent-pale: #f3e48a;
    --mic-dark: #1d2a33;
    --mic-gold: #b38b3c;
  }
  * { margin: 0; padding: 0; box-sizing: border-box; }
  html, body { width: 1200px; height: 1000px; overflow: hidden; }
  body { background: var(--page-bg); position: relative; font-family: "Catamaran", sans-serif; }

  .cover {
    position: absolute;
    top: 187px;
    width: 486px;
    height: 673px;
    background: linear-gradient(160deg, var(--cover-light) 0%, var(--cover-mid) 45%, var(--cover-deep) 100%);
    overflow: hidden;
  }
  .cover--back { left: 47px; }
  .cover--front { left: 667px; }

  /* Back cover */
  .blurb {
    position: absolute;
    left: 37px;
    top: 60px;
    width: 412px;
    color: var(--ink-white);
    font-size: 12.6px;
    line-height: 16.6px;
    text-align: justify;
  }
  .blurb p + p { margin-top: 16px; }
  .back-mic { position: absolute; left: 40px; top: 518px; width: 120px; height: 155px; }

  /* Front cover */
  .title {
    position: absolute;
    left: 0; right: 0; top: 52px;
    text-align: center;
    font-family: "Barlow Semi Condensed", sans-serif;
    font-weight: 700;
    color: var(--ink-white);
    text-transform: uppercase;
    line-height: 1;
    padding-left: 6px;
  }
  .title__pre, .title__post { display: block; font-size: 31px; }
  .title__main { display: block; font-size: 48px; margin: 6px 0 3px; line-height: 48px; }
  .title__post { margin-top: 6px; }

  .subtitle {
    position: absolute;
    left: 0; right: 0; top: 248px;
    text-align: center;
    color: var(--accent-yellow);
    font-size: 19px;
    font-weight: 600;
    padding-left: 6px;
  }

  .callout {
    position: absolute;
    right: 34px; top: 382px;
    text-align: right;
    color: var(--ink-white);
    font-family: "Barlow Semi Condensed", sans-serif;
    font-style: italic;
    font-weight: 600;
    font-size: 16.5px;
    line-height: 20px;
  }
  .callout__source { font-style: normal; font-weight: 600; }

  .front-mic { position: absolute; left: 172px; top: 358px; width: 230px; height: 315px; }

  .authors-rule { position: absolute; left: 0; top: 564px; width: 221px; height: 2px; background: var(--ink-white); }
  .authors { position: absolute; left: 37px; top: 575px; color: var(--accent-pale); }
  .authors__label { font-size: 14px; font-weight: 700; color: var(--accent-yellow); letter-spacing: 0.3px; line-height: 18px; }
  .authors__name { font-size: 18px; font-weight: 500; line-height: 22px; }
</style>
</head>
<body>

  <section class="cover cover--back" aria-label="Back cover">
    <div class="blurb">
      <p>Why do some law firms have the best reputations or command the highest hourly rates? Why are some the go-to firms or thought leaders in particular specialties? Why are your competitors in the media more than you? Two words: Public relations.</p>
      <p>The co-authors are known worldwide as leaders in public relations, legal marketing, and branding. Neil Stamford is called, “A PR Guru.” Bar Ledger magazine wrote ““Many people consider Dale Warbeck to be the nation’s foremost expert on law firm marketing.”Tad Lurvey built Brommick into the first firm to generate $1 billion in revenue. Yvonne Pelstrup is the nation’s go-to lawyer for women’s issues.</p>
      <p>Your home town’s top PI lawyer gets the first look at the biggest cases. Why? Strategic, intentional, effective PR. Are you tired of toiling in anonymity? Want to earn the attention of reporters and editors who can build your credentials and reputation for expertise? Wouldn’t it be nice to have more clients begging you to represent them because they heard you were the best in town? That is what public relations is designed to do.</p>
      <p>Want to get more respect, earn more clients, and charge higher rates? Get known as a thought leader in a specialty practice or industry? Public relations could be your most-important marketing tool. And this book will teach you precisely how. Ready to catapult your practice to new heights? Take a deep breath and dive in….</p>
    </div>
    <svg class="back-mic" viewBox="0 0 120 155" role="img" aria-label="Photo of a small gold and black microphone on a stand">
      <defs>
        <linearGradient id="backMicTone" x1="0" y1="0" x2="0" y2="1">
          <stop offset="0" stop-color="var(--mic-gold)" stop-opacity="0.55"/>
          <stop offset="1" stop-color="var(--mic-dark)" stop-opacity="0.55"/>
        </linearGradient>
      </defs>
      <rect x="0" y="0" width="120" height="155" rx="6" fill="url(#backMicTone)"/>
    </svg>
  </section>

  <section class="cover cover--front" aria-label="Front cover">
    <h1 class="title">
      <span class="title__pre">The Complete</span>
      <span class="title__main">Press Outreach<br>Manual</span>
      <span class="title__post">for Attorneys</span>
    </h1>
    <p class="subtitle">Make Millions using Media and the Internet</p>

    <svg class="front-mic" viewBox="0 0 230 315" role="img" aria-label="Photo of a gold and black microphone on a stand">
      <defs>
        <linearGradient id="frontMicTone" x1="0" y1="0" x2="0" y2="1">
          <stop offset="0" stop-color="var(--mic-gold)" stop-opacity="0.6"/>
          <stop offset="1" stop-color="var(--mic-dark)" stop-opacity="0.6"/>
        </linearGradient>
      </defs>
      <rect x="0" y="0" width="230" height="315" rx="8" fill="url(#frontMicTone)"/>
    </svg>

    <blockquote class="callout">
      “The definitive PR book.<br>
      Simple and powerful.”<br>
      <span class="callout__source">– Tad Lurvey</span>
    </blockquote>

    <div class="authors-rule"></div>
    <div class="authors">
      <p class="authors__label">CO-AUTHORS</p>
      <p class="authors__name">Dale Warbeck, JD</p>
      <p class="authors__name">Neil Stamford</p>
    </div>
  </section>

</body>
</html>
```